Dermatology Flyers - 3 x A4 folded to DL flyers

I need 3 different flyers for my 3 brands for patients to know what we do. The three flyers are for the following three brands:
1. Pellucid Skin Centres Australia
2. Calmderm Rooms Australia
3. Flaketon Care Australia

I'd like to include information about (1) who we are (dermatologist led, dr kiravel Tunstadine) (2) what we do (our mission, our treatments) (3) process to see us (see about us page on website)

websites are:
pellucidcentres.com.au
flaketoncare.com.au
calmdermroomsaustralia.com.au

and logos are attached

we plan to be australia wide group of clinics, so I don't want any location information on the flyer, just the website addresses

if we can incorporate: "learn more about our sister companies" with the logos and websites of the other two brands on the back page of each flyer that would be great

please contact me if you'd like any further information

Industry/Entity Type

Medical, Dermatology

Requirements
Must have
• 3 flyers, size a4 folded to DL

```html
<!DOCTYPE html>
<html lang="en">
<head>
<meta charset="utf-8">
<title>Calmderm Rooms Australia – DL Flyer</title>
<link rel="stylesheet" href="https://fonts.googleapis.com/css2?family=Alfa+Slab+One&family=Arvo:wght@700&family=Arimo:wght@400;700&display=swap">
<style>
  :root {
    --green: #21a348;
    --ink: #1f2a24;
    --text: #2b2b2b;
    --paper: #ffffff;
    --stage: #e9e9e9;
    --orange: #e27d2a;
    --plum: #7a2f36;
    --photo-light: #eef0ef;
    --photo-mid: #d4dad7;
  }
  * { box-sizing: border-box; margin: 0; padding: 0; }
  html, body { width: 1200px; height: 4000px; overflow: hidden; }
  body { background: var(--stage); font-family: "Arimo", Arial, sans-serif; color: var(--text); position: relative; }

  .spread { position: absolute; left: 100px; width: 1000px; height: 707px; background: var(--paper); box-shadow: 0 10px 30px rgba(0,0,0,.12); overflow: hidden; }
  .spread--outside { top: 1000px; }
  .spread--inside { top: 1900px; }
  .panel { position: absolute; top: 0; width: 333.33px; height: 707px; }
  .panel--a { left: 0; }
  .panel--b { left: 333.33px; }
  .panel--c { left: 666.66px; }

  .section-title { font-weight: 700; color: var(--green); font-size: 14px; line-height: 1.2; margin-bottom: 10px; text-transform: uppercase; }
  .section-title--light { color: #fff; }
  .body-copy { font-size: 9.6px; line-height: 1.38; text-align: justify; margin-bottom: 9px; }
  .body-copy--light { color: #fff; text-align: left; }
  .body-copy--left { text-align: left; }
  .text-block { position: absolute; left: 30px; right: 30px; }

  .photo { position: absolute; background: linear-gradient(180deg, var(--photo-light), var(--photo-mid)); }
  .green-block { position: absolute; left: 0; right: 0; background: var(--green); }

  .sister-heading { position: absolute; top: 36px; left: 0; right: 0; text-align: center; }
  .sister-heading .kicker { font-family: "Arvo", serif; font-weight: 700; font-size: 15px; letter-spacing: 1.5px; color: var(--ink); text-transform: uppercase; }
  .sister-heading .headline { font-family: "Alfa Slab One", serif; font-size: 27px; line-height: 1.05; color: var(--green); letter-spacing: 1px; text-transform: uppercase; margin-top: 2px; }

  .brand-name { font-family: "Arvo", serif; font-weight: 700; text-transform: uppercase; text-align: center; letter-spacing: 1px; }
  .sister-brand { position: absolute; left: 0; right: 0; text-align: center; }
  .sister-brand .brand-name { font-size: 17px; }
  .sister-brand--flaketon .brand-name { color: var(--orange); }
  .sister-brand--pellucid .brand-name { color: var(--plum); }
  .web-icon { display: block; margin: 10px auto 6px; }
  .url { font-size: 9.5px; color: var(--text); text-align: center; letter-spacing: .3px; }
  .url--light { color: #fff; }

  .contact-block { position: absolute; left: 0; right: 0; top: 470px; text-align: center; }
  .contact-block .brand-name { color: #fff; font-size: 20px; }

  .cover-brand { position: absolute; top: 24px; left: 60px; right: 10px; color: var(--green); font-size: 19px; line-height: 1.15; }
  .cover-headline { position: absolute; top: 472px; left: 0; right: 0; text-align: center; font-family: "Alfa Slab One", serif; font-weight: 400; color: var(--ink); text-transform: uppercase; line-height: 1.05; }
  .cover-headline .line-sm { font-size: 17px; display: block; }
  .cover-headline .line-lg { font-size: 28px; display: block; }
  .cover-copy { position: absolute; top: 612px; left: 40px; right: 40px; text-align: center; color: #fff; font-size: 10px; line-height: 1.4; }

  .treatment-list { list-style: none; font-size: 9.6px; line-height: 1.38; }
</style>
</head>
<body>

<section class="spread spread--outside">
  <div class="panel panel--a">
    <div class="text-block" style="top:40px;">
      <h3 class="section-title">About Calmderm<br>Rooms Australia</h3>
      <p class="body-copy">With more than a decade of experience helping eczema patients, Dr Kiravel Tunstadine's passion lies in providing access to dermatologist treatment programs and teams in locations that are convenient to patients.</p>
      <p class="body-copy">This began with patients spread across many regional communities, where Dr Tunstadine found that a patient's ability to attend and commit to medical treatment plans was hindered by the large distances that needed to be regularly travelled to access health-care.</p>
      <p class="body-copy">With a strong conviction that medical treatments should be accessible to all, not just those in the heart of the city, the Tunstadines have paved the way in developing a network of clinics to provide local access to treatments for their patients.</p>
      <p class="body-copy">Our network of Calmderm Rooms Australia clinics is now growing Australia wide. Please let us know if you would like a clinic near you by registering your vote on our website!</p>
      <h3 class="section-title" style="margin-top:18px;">Review in Clinic</h3>
      <p class="body-copy">Come to your local clinic for your free appointment with our dermatologist trained staff. They will provide you with information prepared specifically for your condition by Dr Tunstadine, specialist dermatologist, that you will watch and read in clinic with our dermatologist trained staff. You will then be given a full medical history review by our staff, using the protocols developed by specialist dermatologist, Dr Kiravel Tunstadine.</p>
      <h3 class="section-title" style="margin-top:18px;">How we work.</h3>
      <p class="body-copy">We have a tried &amp; tested model of being able to bring safe, cost effective, specialist medical care to a location convenient to you.</p>
    </div>
  </div>

  <div class="panel panel--b">
    <div class="sister-heading">
      <div class="kicker">Learn more about</div>
      <div class="headline">Our sister<br>companies</div>
    </div>
    <div class="sister-brand sister-brand--flaketon" style="top:160px;">
      <div class="brand-name">Flaketon Care<br>Australia</div>
      <svg class="web-icon" width="22" height="22" viewBox="0 0 24 24" fill="none" stroke="#2b2b2b" stroke-width="1.6"><circle cx="12" cy="12" r="10"/><ellipse cx="12" cy="12" rx="4.5" ry="10"/><line x1="2" y1="12" x2="22" y2="12"/><line x1="4" y1="6.5" x2="20" y2="6.5"/><line x1="4" y1="17.5" x2="20" y2="17.5"/></svg>
      <div class="url">flaketoncare.com.au</div>
    </div>
    <div class="sister-brand sister-brand--pellucid" style="top:290px;">
      <div class="brand-name">Pellucid Skin Centres<br>Australia</div>
      <svg class="web-icon" width="22" height="22" viewBox="0 0 24 24" fill="none" stroke="#2b2b2b" stroke-width="1.6"><circle cx="12" cy="12" r="10"/><ellipse cx="12" cy="12" rx="4.5" ry="10"/><line x1="2" y1="12" x2="22" y2="12"/><line x1="4" y1="6.5" x2="20" y2="6.5"/><line x1="4" y1="17.5" x2="20" y2="17.5"/></svg>
      <div class="url">pellucidcentres.com.au</div>
    </div>
    <div class="green-block" style="top:450px; bottom:0;"></div>
    <div class="contact-block">
      <div class="brand-name">Calmderm Rooms<br>Australia</div>
      <svg class="web-icon" width="24" height="18" viewBox="0 0 24 18" fill="#fff"><rect x="0" y="0" width="24" height="18" rx="1"/><path d="M1 1 L12 10 L23 1" fill="none" stroke="#21a348" stroke-width="1.8"/></svg>
      <div class="url url--light">admin@calmdermroomsaustralia.com.au</div>
      <svg class="web-icon" width="22" height="22" viewBox="0 0 24 24" fill="none" stroke="#fff" stroke-width="1.6"><circle cx="12" cy="12" r="10"/><ellipse cx="12" cy="12" rx="4.5" ry="10"/><line x1="2" y1="12" x2="22" y2="12"/><line x1="4" y1="6.5" x2="20" y2="6.5"/><line x1="4" y1="17.5" x2="20" y2="17.5"/></svg>
      <div class="url url--light">calmdermroomsaustralia.com.au</div>
    </div>
  </div>

  <div class="panel panel--c">
    <div class="photo" style="left:0; right:0; top:0; height:450px; background:linear-gradient(180deg,#f2f3f3 0%,#dfe5e3 60%,#2a9d9a 100%);" role="img" aria-label="Smiling nurse in teal scrubs with stethoscope, arms crossed, in a bright clinic"></div>
    <div class="brand-name cover-brand">Calmderm Rooms<br>Australia</div>
    <div class="green-block" style="top:450px; bottom:0;"></div>
    <h1 class="cover-headline">
      <span class="line-sm">Led by</span>
      <span class="line-sm">Dermatologists</span>
      <span class="line-lg">Supported</span>
      <span class="line-sm">Locally near you</span>
    </h1>
    <p class="cover-copy">Access support &amp; treatments close to home, no matter where you live. Providing access to specialist plans and treatments outside of capital cities</p>
  </div>
</section>

<section class="spread spread--inside">
  <div class="panel panel--a">
    <div class="text-block" style="top:34px;">
      <h3 class="section-title">Topical Therapy</h3>
      <p class="body-copy">Topical therapies are creams and lotions that can be applied to skin to assist in repigmentation in vitiligo.</p>
      <p class="body-copy">These may range from topical steroids to anti inflammatory medications to newer generation biologic compounds.</p>
      <p class="body-copy">If a patient's vitiligo has progressed to most of their body, then an option to depigment and even out the colour of the whole body is an option.</p>
      <p class="body-copy">These will require a consultation with your specialist and a prescription.</p>
      <h3 class="section-title" style="margin-top:16px;">Our Eczema Treatments</h3>
      <p class="body-copy">The best components for eczema patients to support their skin is to :</p>
      <ol class="treatment-list">
        <li>1. Use moisturiser to keep moisture in ALL. THE. TIME.</li>
        <li>2. Use a good home care program to keep your skin intact and not aggravate or induce flares.</li>
        <li>3. Use topical therapy &amp; UVB phototherapy to address the flares as required.</li>
        <li>4. Use antihistamines to reduce the itch if you can't sleep,</li>
        <li>5. Use antibiotics to address any infections that have been able to penetrate your skin, and</li>
        <li>6. Use biologics for severe eczema if required.</li>
      </ol>
    </div>
    <div class="photo" style="left:0; right:0; top:555px; bottom:0; background:linear-gradient(135deg,#e8eef2,#c9d6de);" role="img" aria-label="Doctor in a mask examining a patient's arm at a clinic desk"></div>
  </div>

  <div class="panel panel--b">
    <div class="green-block" style="top:330px; height:110px;"></div>
    <div class="photo" style="left:0; right:0; top:0; height:330px; background:linear-gradient(180deg,#eef0ef,#d6dbd9);" role="img" aria-label="Nurse in blue scrubs beside an elderly man in a wheelchair"></div>
    <div class="text-block" style="top:480px;">
      <h3 class="section-title">Home Care Programme</h3>
      <p class="body-copy">Our home care program is designed to support our patients through their vitiligo journey, no matter what age or stage they are experiencing</p>
      <p class="body-copy">Custom designed by specialists to provide dermatological, psychological and practical guidance with information and products required to manage your vitiligo at home, our home care programme is the first time patients can access such an offering in their own home. Ask us more about our home care program when you visit us in clinic.</p>
    </div>
  </div>

  <div class="panel panel--c">
    <div class="photo" style="left:0; right:0; top:0; height:290px; background:linear-gradient(180deg,#eef2f5,#cfd9e0);" role="img" aria-label="Group of smiling medical staff in white coats and scrubs"></div>
    <div class="green-block" style="top:290px; height:150px;"></div>
    <div class="text-block" style="top:312px;">
      <h3 class="section-title section-title--light">Systemic &amp; Biologic</h3>
      <p class="body-copy body-copy--light">Prescription oral medication is the last line of defence on late stage psoriasis that is not relieved by other treatment modalities. To access oral medication, all other treatments must have failed and a severity of psoriasis must be indicated.</p>
    </div>
    <div class="text-block" style="top:480px;">
      <h3 class="section-title">UVB Phototherapy</h3>
      <p class="body-copy body-copy--left">UVB phototherapy has been used with great success in the repigmentation of vitiligo patients. It works by suppressing the immune response that causes the loss of melanocytes, as well as activates functioning melanocytes to produce more pigment.</p>
      <p class="body-copy body-copy--left">Regular treatment, usually 3 times per week for 4 months to begin with, is required. If there is success of repigmentation within this period, then treatment continues until repigmentation is satisfactory and can continue for as long as required.</p>
    </div>
  </div>
</section>

</body>
</html>
```